Lantern Business Cards

Need business cards for my employees at my restaurant.

Needs to include:
Our Logo
Lantern Bowls & Brews
Name: Nora Pettigrew
Title : Owner
Address: 487 Mirella Ave. Lake Havasu City, AZ 86519
Web: www.lanternkestrel.com
Phone: 928-555-0147
Cell: 928-555-0192
Email: info@lanternkestrel.com

```html
<!DOCTYPE html>
<html lang="en">
<head>
<meta charset="utf-8">
<title>Lantern Bowls &amp; Brews – Business Card</title>
<link rel="stylesheet" href="https://fonts.googleapis.com/css2?family=Fira+Sans:wght@700&family=Montserrat:wght@400;500;600&display=swap">
<style>
  :root {
    --bg: #3a3a3a;
    --card-white: #ffffff;
    --brand-red: #c3192e;
    --brand-red-dark: #a8152a;
    --brand-red-light: #d02640;
    --emboss-red: #b01428;
    --ink: #1d1d1d;
    --rule-grey: #8a8a8a;
    --edge-black: #121212;
  }
  * { box-sizing: border-box; margin: 0; padding: 0; }
  html, body { width: 1200px; height: 900px; overflow: hidden; }
  body {
    background: radial-gradient(circle at 50% 45%, #4a4a4a 0%, var(--bg) 55%, #242424 100%);
    font-family: "Montserrat", sans-serif;
    color: var(--ink);
    position: relative;
  }
  .card {
    position: absolute;
    left: 285px;
    width: 630px;
    height: 360px;
    border-radius: 22px;
    overflow: hidden;
    box-shadow: 0 14px 30px rgba(0,0,0,.45);
  }
  /* Front side */
  .card-front { top: 60px; background: var(--card-white); }
  .front-band {
    position: absolute; left: 0; right: 0; bottom: 0; height: 12px;
    background: var(--edge-black);
    border-top: 5px solid var(--brand-red);
  }
  .name-tab {
    position: absolute; left: 0; top: 34px; width: 14px; height: 40px;
    background: var(--brand-red);
  }
  .person { position: absolute; left: 34px; top: 30px; }
  .person-name {
    font-family: "Fira Sans", sans-serif; font-weight: 700;
    font-size: 27px; letter-spacing: .5px; text-transform: uppercase;
    color: var(--brand-red); line-height: 1.05;
  }
  .person-title { font-size: 15px; font-weight: 400; margin-top: 2px; }
  .person-rule {
    width: 150px; height: 2px; background: var(--brand-red); margin-top: 12px;
  }
  .contact-list { list-style: none; margin-top: 12px; }
  .contact-list li {
    display: flex; align-items: center; gap: 9px;
    font-size: 14px; line-height: 24px; font-weight: 500;
  }
  .contact-list svg { width: 12px; height: 12px; fill: var(--brand-red); flex: none; }
  .divider {
    position: absolute; left: 184px; top: 91px; width: 176px; height: 1px;
    background: var(--rule-grey);
  }
  .brand {
    display: flex; flex-direction: column; align-items: center;
    font-family: "Fira Sans", sans-serif; font-weight: 700;
    color: var(--brand-red);
  }
  .brand-line { display: flex; align-items: center; gap: 14px; }
  .brand-dot { width: 40px; height: 40px; border-radius: 50%; background: var(--brand-red); }
  .brand-name {
    font-size: 50px; line-height: 1; text-transform: uppercase; letter-spacing: 1px;
  }
  .brand-tagline {
    font-size: 13px; letter-spacing: 3px; text-transform: uppercase;
    margin-top: 6px;
  }
  .brand-front { position: absolute; right: 36px; top: 34px; }
  .address {
    position: absolute; right: 60px; top: 196px;
    font-size: 19px; line-height: 27px; text-align: right; font-weight: 400;
    font-style: normal;
  }
  /* Back side */
  .card-back {
    top: 480px;
    background: linear-gradient(135deg, var(--brand-red-dark) 0%, var(--brand-red) 50%, var(--brand-red-light) 100%);
    display: flex; align-items: center; justify-content: center;
  }
  .card-back .brand { color: var(--emboss-red); }
  .card-back .brand-dot { width: 52px; height: 52px; background: var(--emboss-red); }
  .card-back .brand-name { font-size: 66px; }
  .card-back .brand-tagline { font-size: 16px; margin-top: 8px; }
</style>
</head>
<body>
  <section class="card card-front" aria-label="Business card front">
    <div class="name-tab"></div>
    <div class="person">
      <h1 class="person-name">Nora Pettigrew</h1>
      <p class="person-title">Owner</p>
      <div class="person-rule"></div>
      <ul class="contact-list">
        <li><svg viewBox="0 0 24 24"><path d="M6.6 10.8a15 15 0 0 0 6.6 6.6l2.2-2.2a1 1 0 0 1 1-.25 11.4 11.4 0 0 0 3.6.6 1 1 0 0 1 1 1V20a1 1 0 0 1-1 1A17 17 0 0 1 3 4a1 1 0 0 1 1-1h3.5a1 1 0 0 1 1 1 11.4 11.4 0 0 0 .6 3.6 1 1 0 0 1-.25 1z"/></svg>928-555-0147</li>
        <li><svg viewBox="0 0 24 24"><rect x="6" y="1" width="12" height="22" rx="2.5"/></svg>928-555-0192</li>
        <li><svg viewBox="0 0 24 24"><path d="M2 5h20v14H2z M2 5l10 8 10-8" /></svg>info@lanternkestrel.com</li>
        <li><svg viewBox="0 0 24 24"><circle cx="12" cy="12" r="10"/></svg>www.lanternkestrel.com</li>
      </ul>
    </div>
    <div class="divider"></div>
    <div class="brand brand-front">
      <div class="brand-line">
        <span class="brand-dot"></span>
        <span class="brand-name">Lantern</span>
      </div>
      <span class="brand-tagline">Bowls &amp; Brews</span>
    </div>
    <address class="address">487 Mirella Ave<br>Lake Havasu City<br>AZ 86519</address>
    <div class="front-band"></div>
  </section>

  <section class="card card-back" aria-label="Business card back">
    <div class="brand">
      <div class="brand-line">
        <span class="brand-dot"></span>
        <span class="brand-name">Lantern</span>
      </div>
      <span class="brand-tagline">Bowls &amp; Brews</span>
    </div>
  </section>
</body>
</html>
```